QRVoltana Wendlio Mobile Experience

Design the following Observation and Care Path mobile app pages so they are very modern, cool and engaging.
We would also like to modernize our current splash experience (attached).

Observation and Care Path wireframes:
https://k4mzq2.plorvex.com/#g=1&p=observations__-_categories

DO NOT SUBMIT LOGO REDESIGNS. Submit all screens for the above wireframes. If you can improve the Splash screen this is a bonus. Use the same color scheme and logo.

Competitive sample:
https://apps.trivelstore.com/store/apps/details?id=com.zorquin.iphone

```html
<!DOCTYPE html>
<html lang="en">
<head>
<meta charset="utf-8">
<title>Visit Details</title>
<link rel="stylesheet" href="https://fonts.googleapis.com/css2?family=Raleway:wght@500;600;700;800&display=swap">
<style>
  :root {
    --page-bg: #f4f4f4;
    --screen-bg: #e4e8ec;
    --orange: #eb7f3e;
    --orange-light: #ef9258;
    --slate: #5f8396;
    --ring: #d5dadf;
    --ink: #2b2b2b;
    --white: #ffffff;
    --divider: #cfd5da;
  }
  * { box-sizing: border-box; margin: 0; padding: 0; }
  html, body { width: 1200px; height: 982px; overflow: hidden; }
  body {
    background: var(--page-bg);
    font-family: "Raleway", sans-serif;
    position: relative;
  }
  .app-screen {
    position: absolute;
    left: 390px; top: 117px;
    width: 420px; height: 748px;
    background: var(--screen-bg);
    overflow: hidden;
    box-shadow: 0 20px 50px rgba(0,0,0,.12);
  }
  .app-header { background: var(--orange); color: var(--white); }
  .status-bar {
    height: 24px; display: flex; align-items: center; justify-content: space-between;
    padding: 0 12px; font-size: 11px; font-weight: 600; color: rgba(255,255,255,.75);
  }
  .signal { display: flex; align-items: center; gap: 3px; }
  .signal i { width: 6px; height: 6px; border-radius: 50%; background: rgba(255,255,255,.75); display: block; }
  .signal i.off { background: none; border: 1px solid rgba(255,255,255,.75); }
  .battery { display: flex; align-items: center; gap: 5px; }
  .battery-cell { width: 24px; height: 10px; border: 1px solid rgba(255,255,255,.75); border-radius: 2px; padding: 1px; }
  .battery-cell span { display: block; height: 100%; background: rgba(255,255,255,.75); }
  .nav-bar {
    height: 52px; display: flex; align-items: center; justify-content: space-between; padding: 0 14px;
  }
  .back { font-size: 12px; font-weight: 600; display: flex; align-items: center; gap: 6px; width: 80px; }
  .title { font-size: 20px; font-weight: 700; letter-spacing: .3px; }
  .nav-actions { display: flex; align-items: center; gap: 16px; width: 80px; justify-content: flex-end; }
  .tabs { display: flex; height: 40px; }
  .tab {
    flex: 1; display: flex; align-items: center; justify-content: center;
    font-size: 14px; font-weight: 600; color: var(--white);
  }
  .tab.active { border-bottom: 3px solid var(--slate); }
  .tab.secondary { background: var(--orange-light); }

  .clock-panel { position: relative; height: 300px; }
  .clock {
    position: absolute; width: 134px; height: 134px; border-radius: 50%;
    border: 9px solid var(--ring); background: var(--screen-bg);
    display: flex; align-items: center; justify-content: center;
  }
  .clock-face {
    width: 104px; height: 104px; border-radius: 50%; background: var(--slate); color: var(--white);
    display: flex; flex-direction: column; align-items: center; justify-content: center; line-height: 1.25;
  }
  .clock-date { font-size: 13px; font-weight: 700; }
  .clock-date b { font-size: 17px; }
  .clock-time { font-size: 11px; font-weight: 700; }
  .clock-label { font-size: 13px; font-weight: 700; }
  .clock-in { left: 48px; top: 22px; }
  .clock-out { right: 28px; top: 110px; }
  .confirmed {
    position: absolute; left: 38px; top: 170px; font-size: 10px; font-weight: 600; color: var(--ink);
    display: flex; align-items: center; gap: 10px;
  }
  .confirmed .dot { width: 13px; height: 13px; border-radius: 50%; background: var(--orange); }
  .submit-button {
    position: absolute; left: 26px; top: 214px; width: 240px; height: 48px; border-radius: 24px;
    background: var(--slate); color: var(--white); font-size: 14px; font-weight: 700;
    display: flex; align-items: center; justify-content: center;
  }

  .tasks-band {
    background: var(--orange); color: var(--white); height: 46px;
    display: flex; align-items: center; justify-content: space-between; padding: 0 18px 0 22px;
  }
  .tasks-title { font-size: 20px; font-weight: 700; }
  .task-list { list-style: none; }
  .task {
    height: 42px; display: flex; align-items: center; padding: 0 22px;
    border-bottom: 1px solid var(--divider); font-size: 13px; font-weight: 700; color: var(--ink);
  }
  .task-code { width: 70px; font-size: 11px; }
  .task.empty { border-bottom-color: #d9dee2; }
</style>
</head>
<body>
  <main class="app-screen">
    <header class="app-header">
      <div class="status-bar">
        <div class="signal"><i></i><i></i><i></i><i></i><i class="off"></i><span>&nbsp;FFF</span>
          <svg width="14" height="10" viewBox="0 0 14 10" style="margin-left:8px"><path d="M1 4a9 9 0 0 1 12 0M3.5 6.5a5 5 0 0 1 7 0M7 9h0" fill="none" stroke="rgba(255,255,255,.75)" stroke-width="1.5" stroke-linecap="round"/></svg>
        </div>
        <div class="battery"><span>100%</span><div class="battery-cell"><span></span></div></div>
      </div>
      <div class="nav-bar">
        <div class="back">
          <svg width="8" height="12" viewBox="0 0 8 12"><path d="M6 1 1.5 6 6 11" fill="none" stroke="#fff" stroke-width="2"/></svg>
          Back
        </div>
        <h1 class="title">Visit Details</h1>
        <div class="nav-actions">
          <svg width="20" height="20" viewBox="0 0 20 20" aria-label="Help"><circle cx="10" cy="10" r="8.5" fill="none" stroke="#fff" stroke-width="2"/><path d="M7.5 8a2.5 2.5 0 1 1 3.5 2.3c-.7.3-1 .8-1 1.5" fill="none" stroke="#fff" stroke-width="2" stroke-linecap="round"/><circle cx="10" cy="14.6" r="1.1" fill="#fff"/></svg>
          <svg width="18" height="18" viewBox="0 0 18 18" aria-label="Add"><path d="M9 2v14M2 9h14" stroke="#fff" stroke-width="3"/></svg>
        </div>
      </div>
      <nav class="tabs">
        <div class="tab active">Clock In / Out</div>
        <div class="tab secondary">Directions</div>
      </nav>
    </header>

    <section class="clock-panel">
      <div class="clock clock-in">
        <div class="clock-face">
          <span class="clock-date">OCT <b>23</b></span>
          <span class="clock-time">12:00 Am</span>
          <span class="clock-label">Clock In</span>
        </div>
      </div>
      <div class="confirmed"><span class="dot"></span>Confirmed: 12:04</div>
      <div class="clock clock-out">
        <div class="clock-face">
          <span class="clock-date">OCT <b>23</b></span>
          <span class="clock-time">12:00 Am</span>
          <span class="clock-label">Clock Out</span>
        </div>
      </div>
      <div class="submit-button">Submit Observation</div>
    </section>

    <section class="tasks">
      <div class="tasks-band">
        <h2 class="tasks-title">Plan of Care Tasks</h2>
        <svg width="12" height="8" viewBox="0 0 12 8"><path d="M1 1.5 6 6.5 11 1.5" fill="none" stroke="#fff" stroke-width="2"/></svg>
      </div>
      <ul class="task-list">
        <li class="task"><span class="task-code">100</span>Bathing</li>
        <li class="task"><span class="task-code">101</span>Bathroom Assistance</li>
        <li class="task"><span class="task-code">102</span>Grooming</li>
        <li class="task"><span class="task-code">103</span>Cooking</li>
        <li class="task"><span class="task-code">104</span>Cleaning</li>
        <li class="task empty"></li>
      </ul>
    </section>
  </main>
</body>
</html>
```